Design new marketing postcard for mortgage loan applicants

I have provided a postcard recently designed as a possible guide for this project and have attached it. The new text is rough drafted and included. Please feel free to design outside of the old postcard or you can design close to it.

```html
<!DOCTYPE html>
<html lang="en">
<head>
<meta charset="utf-8">
<title>Cash Out Equity Loan Postcard</title>
<link rel="stylesheet" href="https://fonts.googleapis.com/css2?family=Oswald:wght@700&family=Montserrat:wght@400;500;600;700&display=swap">
<style>
:root{
  --navy:#0f3b5f;
  --red:#e31e24;
  --gold:#c9964a;
  --gold-light:#e6c27a;
  --tick:#f2c94c;
  --ink:#3d3d3d;
  --blue-text:#12407a;
  --paper:#ffffff;
  --stage:#e3e3e3;
  --stamp:#d9d9dc;
  --rule:#b9b9b9;
}
*{margin:0;padding:0;box-sizing:border-box}
html,body{width:1200px;height:903px;overflow:hidden;background:var(--stage)}
body{position:relative;font-family:"Montserrat",Arial,sans-serif}
.postcard{
  position:absolute;width:665px;height:444px;background:var(--paper);
  overflow:hidden;transform:scale(.8);transform-origin:0 0;
  box-shadow:0 4px 14px rgba(0,0,0,.18);
}
.postcard--front{left:209px;top:77px}
.postcard--back{left:500px;top:480px}
.postcard__art{position:absolute;inset:0}
.abs{position:absolute}

/* front */
.headline{left:27px;top:28px;font-family:"Oswald",Impact,sans-serif;font-weight:700;
  color:var(--red);font-size:42px;line-height:46px;letter-spacing:.3px;text-transform:uppercase}
.subhead{left:28px;top:127px;font-family:Arial,Helvetica,sans-serif;font-weight:700;
  color:var(--blue-text);font-size:12.5px}
.benefits{left:26px;top:182px;list-style:none}
.benefits li{display:flex;align-items:center;height:27.6px;color:#fff;font-size:15px;font-weight:500}
.benefits svg{width:11px;height:11px;margin-right:10px;flex:none}
.nmls{right:28px;top:351px;color:#fff;font-size:17px;font-weight:500;letter-spacing:.3px}
.call{display:flex;align-items:center;color:#fff;font-weight:700;letter-spacing:.6px}
.call svg{margin:0 12px}
.call--front{right:27px;top:388px;font-size:26px}
.call--front svg{width:26px;height:26px}
.call--back{left:27px;top:392px;font-size:22px}
.call--back svg{width:22px;height:22px}
.brand{display:flex;align-items:center;color:var(--navy);font-weight:700}
.brand__dot{border-radius:50%;background:var(--gold);flex:none}
.brand--front{left:30px;top:370px;font-size:15px}
.brand--front .brand__dot{width:26px;height:26px;margin-right:10px}
.brand--back{left:362px;top:56px;font-size:12.5px;width:200px;line-height:15px}
.brand--back .brand__dot{width:22px;height:22px;margin-right:8px}

/* back */
.message{left:28px;top:34px;width:295px;color:var(--ink);font-size:14px;line-height:16.7px;letter-spacing:.2px}
.disclaimer{left:28px;top:168px;width:300px;color:var(--ink);font-size:11.6px;line-height:14.7px;text-align:justify;letter-spacing:.1px}
.stamp{left:571px;top:28px;width:66px;height:76px;background:var(--stamp)}
.address-line{left:381px;width:256px;height:1px;background:var(--rule)}
</style>
</head>
<body>

<section class="postcard postcard--front" aria-label="Postcard front">
  <svg class="postcard__art" viewBox="0 0 665 444" aria-hidden="false">
    <defs>
      <linearGradient id="photoTone" x1="0" y1="0" x2="1" y2="1">
        <stop offset="0" stop-color="#d3dbe4"/>
        <stop offset=".55" stop-color="#a9bfd6"/>
        <stop offset="1" stop-color="#6f8fb3"/>
      </linearGradient>
      <clipPath id="photoClip"><circle cx="545" cy="175" r="263"/></clipPath>
    </defs>
    <path d="M0 162 Q150 140 300 152 L300 444 L0 444 Z" fill="var(--navy)"/>
    <g role="img" aria-label="Photo of a smiling couple embracing">
      <rect x="260" y="0" width="405" height="444" fill="url(#photoTone)" clip-path="url(#photoClip)"/>
    </g>
    <circle cx="545" cy="175" r="263" fill="none" stroke="var(--gold)" stroke-width="4"/>
    <path d="M0 338 Q180 322 345 388 L345 444 L0 444 Z" fill="var(--paper)"/>
    <path d="M0 338 Q180 322 345 388" fill="none" stroke="var(--gold)" stroke-width="4"/>
    <path d="M212 444 C300 378 450 334 665 324 V444 Z" fill="var(--navy)"/>
    <path d="M212 444 C300 378 450 334 665 324" fill="none" stroke="var(--gold)" stroke-width="4"/>
  </svg>

  <h1 class="abs headline">Cash Out<br>Equity Loan</h1>
  <p class="abs subhead">ON YOUR INVESTMENT PROPERTY</p>
  <ul class="abs benefits">
    <li><svg viewBox="0 0 12 12"><circle cx="6" cy="6" r="6" fill="var(--tick)"/><path d="M3.2 6.2l2 2 3.6-4" stroke="var(--navy)" stroke-width="1.6" fill="none"/></svg>Loan Based on your equity</li>
    <li><svg viewBox="0 0 12 12"><circle cx="6" cy="6" r="6" fill="var(--tick)"/><path d="M3.2 6.2l2 2 3.6-4" stroke="var(--navy)" stroke-width="1.6" fill="none"/></svg>Fast close</li>
    <li><svg viewBox="0 0 12 12"><circle cx="6" cy="6" r="6" fill="var(--tick)"/><path d="M3.2 6.2l2 2 3.6-4" stroke="var(--navy)" stroke-width="1.6" fill="none"/></svg>No Income Qualifying</li>
    <li><svg viewBox="0 0 12 12"><circle cx="6" cy="6" r="6" fill="var(--tick)"/><path d="M3.2 6.2l2 2 3.6-4" stroke="var(--navy)" stroke-width="1.6" fill="none"/></svg>Not based on credit scores</li>
    <li><svg viewBox="0 0 12 12"><circle cx="6" cy="6" r="6" fill="var(--tick)"/><path d="M3.2 6.2l2 2 3.6-4" stroke="var(--navy)" stroke-width="1.6" fill="none"/></svg>Competitive Rates</li>
  </ul>
  <div class="abs brand brand--front"><span class="brand__dot"></span>Harbor Crest Lending, Inc.</div>
  <p class="abs nmls">NMLS #480172</p>
  <p class="abs call call--front">CALL
    <svg viewBox="0 0 24 24"><path d="M6.6 2.5l3 3.2-1.9 2.6c1.2 2.6 3.3 4.7 6 6l2.6-1.9 3.2 3-1.5 3.6C11 19 5 13 2.9 4z" fill="var(--red)"/><path d="M14 3.5a7 7 0 0 1 6.5 6.5M14 7a3.5 3.5 0 0 1 3 3" stroke="var(--red)" stroke-width="1.6" fill="none"/></svg>
    800-555-0148</p>
</section>

<section class="postcard postcard--back" aria-label="Postcard back">
  <svg class="postcard__art" viewBox="0 0 665 444" aria-hidden="true">
    <circle cx="100" cy="170" r="258" fill="none" stroke="var(--gold)" stroke-width="4"/>
    <path d="M0 356 Q250 336 420 444 L0 444 Z" fill="var(--navy)"/>
    <path d="M0 356 Q250 336 420 444" fill="none" stroke="var(--gold)" stroke-width="4"/>
  </svg>

  <p class="abs message">I am pleased to inform you that an equity based loan is available for your investment property. This no qualifying loan is possible simply due to the equity you have. Please call for a quote. You can also email dan@harborcrest.loan</p>
  <p class="abs disclaimer">*Loan is subject to confirmation of equity and is for income property, investment property, or other property business purpose. Other conditions and restrictions apply. Please call for complete program requirements and details. Harbor Crest Lending, Inc. 2280 Lantern Way Suite 102, Fairview CA 90010, Daniel Reyes Ca Dept of Real Estate-Real Estate Broker Lic.#02045517, NMLS # 615390, CA Dept. of Real Estate Lic.# 02287734, NMLS #480172.</p>

  <div class="abs brand brand--back"><span class="brand__dot"></span>Harbor Crest Lending, Inc.</div>
  <div class="abs stamp" aria-label="Stamp area"></div>
  <div class="abs address-line" style="top:207px"></div>
  <div class="abs address-line" style="top:256px"></div>
  <div class="abs address-line" style="top:305px"></div>

  <p class="abs call call--back">CALL
    <svg viewBox="0 0 24 24"><path d="M6.6 2.5l3 3.2-1.9 2.6c1.2 2.6 3.3 4.7 6 6l2.6-1.9 3.2 3-1.5 3.6C11 19 5 13 2.9 4z" fill="var(--red)"/><path d="M14 3.5a7 7 0 0 1 6.5 6.5M14 7a3.5 3.5 0 0 1 3 3" stroke="var(--red)" stroke-width="1.6" fill="none"/></svg>
    800-555-0148</p>
</section>

</body>
</html>
```